Copper Lantern Podcast Business Card Design

Needing a business card with the logo design provided for Copper Lantern Podcast. I am looking for a modern style that fits the current logo.

Info:
Name: Bao Khanh
Title: Creator/Host
Email: bao@copperlanternpod.com
Phone: (405) 637-2918
www.copperlanternpod.com
Twitter: @coplanternpod
Instagram: @copperlanternpodcast
Facebook: Copper Lantern Podcast

Industry/Entity Type

Business

Font styles to use
Sans Serif

Colors
000000
ffffff

Requirements
Must have
• modern, clean design
Nice to have
• social media contact info

```html
<!DOCTYPE html>
<html lang="en">
<head>
<meta charset="utf-8">
<title>Copper Lantern Podcast – Business Card</title>
<link href="https://fonts.googleapis.com/css2?family=Roboto:wght@400;700&display=swap" rel="stylesheet">
<style>
  :root {
    --ink: #000000;
    --paper: #ffffff;
    --backdrop: #d2d2d2;
    --muted: #e6e6e6;
  }
  * { margin: 0; padding: 0; box-sizing: border-box; }
  html, body {
    width: 1200px; height: 801px; overflow: hidden;
    background: var(--backdrop);
    font-family: "Roboto", Arial, sans-serif;
  }
  .stage {
    position: relative; width: 1200px; height: 801px;
    display: flex; align-items: center; justify-content: center; gap: 40px;
  }
  .card {
    position: relative; width: 540px; height: 309px;
    background: var(--ink); color: var(--paper);
    box-shadow: 0 6px 18px rgba(0,0,0,0.25);
  }
  /* front: brand name in place of the mark */
  .card--front { display: flex; align-items: center; justify-content: center; }
  .brand-large {
    display: flex; align-items: center; gap: 16px;
    font-weight: 700; font-size: 34px; letter-spacing: 1px; text-transform: uppercase;
  }
  .brand-square { width: 22px; height: 22px; background: var(--paper); }

  /* back: contact details */
  .brand-small {
    position: absolute; top: 34px; left: 0; right: 0;
    display: flex; flex-direction: column; align-items: center; gap: 5px;
    font-weight: 700; text-transform: uppercase;
  }
  .brand-small .brand-square { width: 14px; height: 14px; }
  .brand-small .brand-name { font-size: 17px; letter-spacing: 0.5px; }
  .brand-small .brand-sub { font-size: 8px; letter-spacing: 5px; font-weight: 400; }

  .person {
    position: absolute; top: 150px; left: 70px; width: 190px; text-align: right;
  }
  .person-name { font-weight: 700; font-size: 17px; letter-spacing: 2px; }
  .person-role { font-size: 10px; letter-spacing: 1px; margin-top: 3px; color: var(--muted); }

  .contacts {
    position: absolute; top: 138px; left: 290px;
    list-style: none; font-size: 11px; letter-spacing: 0.6px;
  }
  .contacts li { display: flex; align-items: center; gap: 9px; height: 18px; }
  .contacts svg { width: 10px; height: 10px; flex: none; }

  .socials {
    position: absolute; bottom: 22px; left: 0; right: 0;
    display: flex; justify-content: center; gap: 22px;
    list-style: none; font-size: 10.5px; font-weight: 700; letter-spacing: 0.6px;
  }
  .socials li { display: flex; align-items: center; gap: 7px; }
  .social-square { width: 12px; height: 12px; background: var(--paper); border-radius: 2px; }
</style>
</head>
<body>
<main class="stage">
  <section class="card card--front" aria-label="Card front">
    <div class="brand-large"><span class="brand-square"></span><span>Copper Lantern</span></div>
  </section>

  <section class="card card--back" aria-label="Card back">
    <div class="brand-small">
      <span class="brand-square"></span>
      <span class="brand-name">Copper Lantern</span>
      <span class="brand-sub">Podcast</span>
    </div>

    <div class="person">
      <p class="person-name">BAO KHANH</p>
      <p class="person-role">CREATOR / HOST</p>
    </div>

    <ul class="contacts">
      <li>
        <svg viewBox="0 0 10 10"><rect x="2" y="0.5" width="6" height="9" rx="1" fill="none" stroke="#fff" stroke-width="1"/></svg>
        (405) 637-2918
      </li>
      <li>
        <svg viewBox="0 0 10 10"><rect x="0.5" y="1.5" width="9" height="7" fill="none" stroke="#fff" stroke-width="1"/><path d="M0.5 1.5 L5 5.5 L9.5 1.5" fill="none" stroke="#fff" stroke-width="1"/></svg>
        bao@copperlanternpod.com
      </li>
      <li>
        <svg viewBox="0 0 10 10"><circle cx="5" cy="5" r="4.3" fill="none" stroke="#fff" stroke-width="1"/><path d="M0.7 5 H9.3 M5 0.7 C2.5 3 2.5 7 5 9.3 M5 0.7 C7.5 3 7.5 7 5 9.3" fill="none" stroke="#fff" stroke-width="0.8"/></svg>
        www.copperlanternpod.com
      </li>
    </ul>

    <ul class="socials">
      <li><span class="social-square"></span>Copper Lantern Podcast</li>
      <li><span class="social-square"></span>@coplanternpod</li>
      <li><span class="social-square"></span>@copperlanternpodcast</li>
    </ul>
  </section>
</main>
</body>
</html>
```